Night Guard Packaging

We have designed a sleek night guard for Bruxism (grinding and clenching) and would like a simple design for the front of the box.
We like simple and clean design, so maybe your artist can draw a clean image of the guard instead of using a photo?

Colours:
Our box will be Matt black, similar to example attached.
We are thinking white/black with a hint of green (the same green as the guard, also attached). The “mock-up” box artist design is the one we are leaning towards (the other examples are to give you a feel for what we like). But, if it’s too elegant it won’t feel “medical”.

The logo will need to be inverted, as it is for a white background (original attached)

Words:
Lumora Night Guard (main heading)
For Grinding & Clenching (sun heading below in smaller font).

We like, symmetry, sleek, clean, elegant, luxurious.

Maybe you artist could draw a clean image of the guard instead of using a photo? I screen shot some images with font and artists impressions. But, the customer will need to be able to see/understand the product, from the minimal details on the front of the box, as they won’t be able to open it.

```html
<!DOCTYPE html>
<html lang="en">
<head>
<meta charset="utf-8">
<title>Night Guard Box Front</title>
<link rel="stylesheet" href="https://fonts.googleapis.com/css2?family=Bebas+Neue&family=Oswald:wght@500&display=swap">
<style>
  :root {
    --box-black: #141414;
    --box-black-edge: #0c0c0c;
    --ink-white: #ffffff;
    --line-white: rgba(255,255,255,0.85);
    --guard-mint: #3fe3c8;
    --guard-deep: #1fb8a0;
  }
  html, body {
    margin: 0;
    width: 1200px;
    height: 1200px;
    overflow: hidden;
  }
  .box-front {
    position: relative;
    width: 1200px;
    height: 1200px;
    background: radial-gradient(circle at 50% 45%, var(--box-black) 0%, var(--box-black) 55%, var(--box-black-edge) 100%);
    font-family: "Bebas Neue", sans-serif;
    color: var(--ink-white);
  }
  .frame {
    position: absolute;
    inset: 0;
  }
  .brand-mark {
    position: absolute;
    left: 511px;
    top: 251px;
    width: 172px;
    height: 172px;
    border: 1.5px solid var(--line-white);
    border-radius: 50%;
    display: flex;
    align-items: center;
    justify-content: center;
  }
  .brand-name {
    font-family: "Oswald", sans-serif;
    font-weight: 500;
    font-size: 26px;
    letter-spacing: 6px;
    color: var(--ink-white);
    padding-left: 6px;
  }
  .product-title {
    position: absolute;
    left: 0;
    right: 0;
    top: 500px;
    margin: 0;
    text-align: center;
    font-size: 152px;
    font-weight: 400;
    line-height: 1;
    letter-spacing: 2px;
  }
  .product-subtitle {
    position: absolute;
    left: 0;
    right: 0;
    top: 664px;
    margin: 0;
    text-align: center;
    font-family: "Oswald", sans-serif;
    font-weight: 500;
    font-size: 26px;
    letter-spacing: 8px;
    line-height: 1;
    padding-left: 8px;
  }
  .guard-visual {
    position: absolute;
    left: 500px;
    top: 775px;
    width: 220px;
    height: 150px;
    border-radius: 40px 60px 50px 40px;
    background: linear-gradient(135deg, var(--guard-mint), var(--guard-deep));
  }
</style>
</head>
<body>
  <main class="box-front">
    <svg class="frame" width="1200" height="1200" viewBox="0 0 1200 1200" aria-hidden="true">
      <g fill="none" stroke="var(--line-white)" stroke-width="2">
        <polyline points="509,337 337,337 337,500"/>
        <polyline points="695,337 863,337 863,500"/>
        <polyline points="337,655 337,863 491,863"/>
        <polyline points="863,655 863,863 713,863"/>
      </g>
    </svg>

    <div class="brand-mark">
      <span class="brand-name">DENVIRA</span>
    </div>

    <h1 class="product-title">NIGHT GUARD</h1>
    <p class="product-subtitle">FOR GRINDING &amp; CLENCHING</p>

    <div class="guard-visual" role="img" aria-label="Mint green translucent night guard mouthpiece"></div>
  </main>
</body>
</html>
```